Update the A4 Specials Page for Restaurant/Cafe

Provide a MINIMALIST attractive Specials page we can print weekly for our food and drink specials to give to our guests. Final design is to be provided in WORD Document so it can be easily edited by Manager. Should be black text and MINIMALIST to minimise ink usage as we print hundreds a week. We have UPLOADED the existing page as a template for you to update. Maybe logo can stay, see what you think. Or delete it and do something else. Keep it simple. Choose a good FONT. Could be a little playful with a cocktail ICON or something. Our existing menus can be seen at www.tallpinebistro.com.au and they are using font Alegreya. Please note we are unable to provide any feedback to designers, however we really do appreciate your time if you are submitting a design. Thank you for your participation.

```html
<!DOCTYPE html>
<html lang="en">
<head>
<meta charset="utf-8">
<title>Tall Pine Bistro – Weekly Specials</title>
<link rel="stylesheet" href="https://fonts.googleapis.com/css2?family=Alegreya:wght@400;700;800&family=Cinzel:wght@600;700&display=swap">
<style>
  :root {
    --paper: #ffffff;
    --canvas: #f1f1f1;
    --ink: #111111;
    --price: #d4141c;
    --name-pink: #e59aa6;
    --name-shade: #8fb3d6;
    --frame-tint: #ecdcd8;
  }
  * { margin: 0; padding: 0; box-sizing: border-box; }
  html, body { width: 856px; height: 1200px; overflow: hidden; background: var(--canvas); }
  .page {
    position: relative;
    width: 856px; height: 1200px;
    background: var(--paper);
    font-family: "Alegreya", "Georgia", serif;
    color: var(--ink);
  }
  .page-frame {
    position: absolute;
    left: 38px; top: 30px; width: 798px; height: 1136px;
    border: 8px solid var(--frame-tint);
  }
  .brand {
    position: absolute; left: 0; right: 0; top: 92px;
    text-align: center;
    font-family: "Alegreya", "Georgia", serif;
    font-weight: 800; font-size: 26px; letter-spacing: 1px;
    color: var(--ink);
  }
  .line {
    position: absolute; left: 0; right: 0;
    text-align: center; font-weight: 700; line-height: 1;
  }
  .section-title {
    font-family: "Cinzel", "Georgia", serif; font-size: 20px; font-weight: 700;
    text-transform: uppercase;
  }
  .section-title--mixed { font-family: "Alegreya", "Georgia", serif; font-size: 23px; font-weight: 800; }
  .item-name { font-size: 17px; text-transform: uppercase; }
  .item-detail { font-size: 17.5px; }
  .price { font-size: 16px; color: var(--price); }
  .feature-name {
    font-family: "Cinzel", "Georgia", serif; font-size: 15px; text-transform: uppercase;
    color: var(--name-pink); text-shadow: 1px 1px 0 var(--name-shade);
  }
</style>
</head>
<body>
<main class="page">
  <div class="page-frame" role="img" aria-label="Light festive border framing the page"></div>

  <div class="brand">TALL PINE BISTRO</div>

  <section class="specials">
    <h1 class="line section-title" style="top:253px">Weekly Specials</h1>
    <p class="line item-name" style="top:296px">Chicken Filo</p>
    <p class="line item-detail" style="top:333px">Creamy Chicken with Pinenuts, wrapped in Filo Pastry.</p>
    <p class="line item-detail" style="top:370px">Served with Side Salad &amp; Zulu Sauce</p>
    <p class="line price" style="top:413px">$24</p>

    <h2 class="line section-title" style="top:487px">Minestrone Soup</h2>
    <p class="line item-detail" style="top:529px">Served with Garlic Bread</p>
    <p class="line price" style="top:568px">$8</p>

    <h2 class="line section-title--mixed" style="top:642px">Cocktail Special</h2>
    <p class="line feature-name" style="top:689px">Passionista</p>
    <p class="line item-detail" style="top:722px">Vodka, Passionfruit Pulp, Mango Puree</p>
    <p class="line item-detail" style="top:757px">Top up with Ginger &amp; Lemon Kombucha</p>
    <p class="line price" style="top:796px">$17</p>

    <h2 class="line section-title--mixed" style="top:868px">Craft Beer Special</h2>
    <p class="line feature-name" style="top:915px">Crooked Heron</p>
    <p class="line item-detail" style="top:951px">SUN BURST</p>
    <p class="line item-detail" style="top:989px">Tropical Pale Ale</p>
    <p class="line item-detail" style="top:1027px">4.8% Alc.</p>
    <p class="line price" style="top:1065px">$10</p>
  </section>
</main>
</body>
</html>
```